Hadley's Labouring Service needs a logo/business cards.

i've just started a new Labouring Business, Called Hadley's Labouring Service, I provide high quality labouring servicing to local Builders and Tradesmen.
I'd like my business cards to reflect the hard work and dedication I put into my business.
I'd like to see Burnt Orange and blacks in the cards and logo.
I want my cards to catch peoples eye as there is A lot of dull business cards in my industry.

Target Market(s)

Builders and other tradesmen

Contact Information for Business Card

Hadley's Labouring Service

Font styles to use
Sans Serif

Colors
f78f20
ffc214
000000
ffffff

Requirements
Must have
• My name : Tom Hadley
• My Number: 0497562083
• Email Address : hadleylabouringservice@examplemail.net
• A Sharp and Professional Design
Nice to have
• A unique design that separates my Cards from others,
• As I try to provide unique service to my clients I'd love my cards/logo to reflect this.

```html
<!DOCTYPE html>
<html lang="en">
<head>
<meta charset="utf-8">
<title>Hadley's Labouring Service – Business Card</title>
<link rel="stylesheet" href="https://fonts.googleapis.com/css2?family=Arimo:wght@400;700&display=swap">
<style>
  :root {
    --ink: #000000;
    --paper: #ffffff;
    --amber: #fbbc34;
    --text-dark: #333333;
    --backdrop: #ececec;
  }
  * { margin: 0; padding: 0; box-sizing: border-box; }
  html, body {
    width: 1200px;
    height: 828px;
    overflow: hidden;
    background: var(--backdrop);
    font-family: "Arimo", Arial, sans-serif;
  }
  .canvas {
    position: relative;
    width: 1200px;
    height: 828px;
  }
  .business-card {
    position: absolute;
    left: 75px;
    top: 115px;
    width: 1050px;
    height: 598px;
    background: var(--paper);
    box-shadow: 0 6px 18px rgba(0,0,0,0.18);
    overflow: hidden;
  }
  .card-shapes {
    position: absolute;
    inset: 0;
    width: 100%;
    height: 100%;
  }
  .card-shapes .band { fill: var(--ink); }
  .card-shapes .accent { fill: var(--amber); }
  .brand-name {
    position: absolute;
    left: 296px;
    top: 114px;
    transform: translateX(-50%);
    font-size: 14px;
    font-weight: 700;
    letter-spacing: 1px;
    text-transform: uppercase;
    color: var(--ink);
    white-space: nowrap;
  }
  .holder-name {
    position: absolute;
    left: 104px;
    top: 246px;
    font-size: 50px;
    line-height: 1;
    font-weight: 400;
    letter-spacing: 4px;
    text-transform: uppercase;
    color: var(--text-dark);
    white-space: nowrap;
  }
  .phone {
    position: absolute;
    left: 691px;
    top: 248px;
    font-size: 40px;
    line-height: 1;
    letter-spacing: 2px;
    color: var(--ink);
    white-space: nowrap;
  }
  .email {
    position: absolute;
    left: 37px;
    top: 455px;
    font-size: 30px;
    line-height: 1;
    letter-spacing: 1px;
    color: var(--text-dark);
    white-space: nowrap;
  }
</style>
</head>
<body>
<main class="canvas">
  <section class="business-card">
    <svg class="card-shapes" viewBox="0 0 1050 598" aria-hidden="true">
      <rect class="band top-band" x="0" y="0" width="1050" height="217"/>
      <rect class="band bottom-band" x="0" y="517" width="1050" height="81"/>
      <polygon class="accent roof-triangle" points="296,4 550,217 50,217"/>
      <polygon class="accent side-wedge" points="550,217 1050,217 1050,517 898,517"/>
    </svg>
    <p class="brand-name">Hadley's Labouring Service</p>
    <h1 class="holder-name">Tom Hadley</h1>
    <p class="phone">0497562083</p>
    <p class="email">hadleylabouringservice@examplemail.net</p>
  </section>
</main>
</body>
</html>
```